Korbel Medical Business Card Design

This is a private medical device company. We recently launched the new website and would like to redesign the business cards. Please see the website: www.korbelmedical-demo.com. We'd like to keep the cards simple and professional but modern to match the website and collateral branding. Our customers are physicians and investors. I have attached the old design for comparison. I have also attached the updated logo. Please note the business card information will change, based on all employees who need to order them. So I will need to be able easily edit the copy.
Updates

Hi designers-thank you very much for submitting designs. I look forward to the results!! Jodi

Target Market(s)

Our target audience are physicians

Industry/Entity Type

Medical

Contact Information for Business Card

Denise Halvorsen
Director of Marketing and Reimbursement
dhalvorsen@korbelmedical-demo.com
M: xxx-xxx-xxxx
O: xxx-xxx-xxxx
4120 Lark Mill Rd.
Suite 380
Austin, TX 78759

Font styles to use
Sans Serif

Requirements
Must have
• Must include the logo and a color or color from the logo and branding
Nice to have
• Maybe include the logo icon on the back.

```html
<!DOCTYPE html>
<html lang="en">
<head>
<meta charset="utf-8">
<title>Korbel Medical Business Card</title>
<link rel="stylesheet" href="https://fonts.googleapis.com/css2?family=Open+Sans:wght@400;600;700&display=swap">
<style>
  :root {
    --backdrop: #ecebe9;
    --card: #ffffff;
    --ink: #3d393a;
    --band: #4a4647;
    --band-text: #ffffff;
    --teal: #5a9fb0;
    --rule: rgba(255,255,255,0.55);
  }
  * { box-sizing: border-box; margin: 0; padding: 0; }
  html, body {
    width: 1200px; height: 1000px; overflow: hidden;
    background: var(--backdrop);
    font-family: "Open Sans", sans-serif;
    color: var(--ink);
  }
  .canvas { position: relative; width: 1200px; height: 1000px; }
  .card {
    position: absolute; left: 265px; width: 666px;
    background: var(--card);
    box-shadow: 0 4px 10px rgba(0,0,0,0.18);
    overflow: hidden;
  }
  .card--front { top: 73px; height: 397px; display: flex; align-items: center; justify-content: center; }
  .card--back { top: 533px; height: 395px; }

  .wordmark { display: flex; align-items: center; gap: 14px; color: var(--ink); font-weight: 600; white-space: nowrap; }
  .wordmark__square { background: var(--teal); flex: none; }
  .wordmark--large { font-size: 54px; letter-spacing: -0.5px; }
  .wordmark--large .wordmark__square { width: 44px; height: 44px; }
  .wordmark--small { font-size: 44px; letter-spacing: -0.5px; }
  .wordmark--small .wordmark__square { width: 36px; height: 36px; }

  .back__brand { position: absolute; top: 48px; left: 0; right: 0; display: flex; justify-content: center; }
  .holder { position: absolute; top: 158px; left: 0; right: 0; text-align: center; }
  .holder__name { font-size: 20px; font-weight: 700; line-height: 26px; }
  .holder__title { font-size: 15.5px; font-weight: 400; line-height: 20px; }

  .contact-band {
    position: absolute; left: 0; right: 0; bottom: 0; height: 145px;
    background: var(--band); color: var(--band-text);
  }
  .address {
    position: absolute; right: 368px; top: 38px; text-align: right;
    font-size: 16px; line-height: 23px;
  }
  .divider {
    position: absolute; left: 333px; top: 30px; width: 1px; height: 78px;
    background: linear-gradient(to bottom, transparent, var(--rule), transparent);
  }
  .contacts { position: absolute; left: 368px; top: 36px; list-style: none; font-size: 15px; line-height: 23px; }
  .contacts li { display: flex; align-items: center; gap: 10px; }
  .contacts svg { width: 13px; height: 13px; flex: none; fill: var(--band-text); }
</style>
</head>
<body>
<main class="canvas">
  <section class="card card--front" aria-label="Card front">
    <div class="wordmark wordmark--large">
      <span class="wordmark__square"></span>
      <span>Korbel Medical</span>
    </div>
  </section>

  <section class="card card--back" aria-label="Card back">
    <div class="back__brand">
      <div class="wordmark wordmark--small">
        <span class="wordmark__square"></span>
        <span>Korbel Medical</span>
      </div>
    </div>

    <div class="holder">
      <p class="holder__name">Denise Halvorsen</p>
      <p class="holder__title">Marketing Director / Reimbursement</p>
    </div>

    <div class="contact-band">
      <address class="address" style="font-style:normal">
        4120 Lark Mill Rd. Suite 380<br>
        Austin, TX 78759
      </address>
      <span class="divider"></span>
      <ul class="contacts">
        <li>
          <svg viewBox="0 0 16 16" aria-label="Mobile"><path d="M4 0h8a1 1 0 0 1 1 1v14a1 1 0 0 1-1 1H4a1 1 0 0 1-1-1V1a1 1 0 0 1 1-1zm1 2v10h6V2zm3 11a1 1 0 1 0 0 2 1 1 0 0 0 0-2z"/></svg>
          <span>xxx - xxx - xxxx</span>
        </li>
        <li>
          <svg viewBox="0 0 16 16" aria-label="Office phone"><path d="M1 5c0-2 3-3 7-3s7 1 7 3v1.5h-4V5H5v1.5H1zM4 8h8l2 6H2zm4 1.5a2 2 0 1 0 0 4 2 2 0 0 0 0-4z"/></svg>
          <span>xxx - xxx - xxxx</span>
        </li>
        <li>
          <svg viewBox="0 0 16 16" aria-label="Email"><path d="M1 3h14v1.2L8 9 1 4.2zm0 2.6 7 4.8 7-4.8V13H1z"/></svg>
          <span>dhalvorsen@korbelmedical-demo.com</span>
        </li>
      </ul>
    </div>
  </section>
</main>
</body>
</html>
```